GUARANTEED WordPress design needed for a sassy, confident charisma coach!

We need a website design for Marla Penrick's brand new, responsive, Wordpress website.
Marla is a trainer / coach who teaches people how to be more charismatic and runs events, publishes video courses and has an ongoing video blog. Her old website is here: www.marlapenrick.co.uk ... but it's now time to have a much better site!
We have a strong idea about the technical components of the website, but we need a designer's eye to create a great style for the site (and provide layered PSD files which our developers will then convert to HTML and CSS).
Marla's brand is sassy, brave, warm and confident. The videos on her existing site give quite a good feel for her personality. We need a clean, stylish and compelling page that isn't too corporate and captures her personality. Every element needs to feel coherent, from fonts and headings to colours and spacing.
The following sites are not exactly what Marla wants (and certainly aren't right in terms of colours) but they give you an idea of the kind of people she is competing against and the area she is operating in:
http://www.tessa-broughley.example/
http://rowanfelsby.example/
Ideally, you will have done something similar and be able to key in on exactly the kind of thing we want: we're not looking to reinvent the wheel. Hopefully you won't mind tweaking a few things if you are close to what we need.
More detail is provided in the word document attached. But in a nutshell we need: a banner, footer, sign-up strap, menu bar, signature and 4 different basic page types. We want bursts of bright colours, contrasted with black and white if possible - sorry we can't be more specific than that...
The word doc also contains some amateur mock-ups as well (the images are also just mockups at this stage) - but although these give a general sense of the structure what we are looking for, we are clearly not designers...so please help! We need a designer's touch!
Kind regards,
Corin
PS The layered PSD versions of the mockup files are available on Cloudvantre: https://files.cloudvantre.example/sh/k72pqa4w1zbtmrd/QXvenlr8Ty3PwMiU6Hs2kYfDb?dl=0
Target Market(s)
Entrepreneurs who need to sell themselves.
Number of Pages Required
4 page

```html
<!DOCTYPE html>
<html lang="en">
<head>
<meta charset="utf-8">
<title>Marla Penrick – Attract Connect Influence</title>
<link href="https://fonts.googleapis.com/css2?family=Roboto:wght@300;400;500;700;900&display=swap" rel="stylesheet">
<style>
:root{
  --red:#e5202a;
  --ink:#2b2b2b;
  --text:#555;
  --muted:#999;
  --page:#ececec;
  --white:#fff;
  --footer:#2e2e2e;
}
*{box-sizing:border-box;margin:0;padding:0}
html,body{width:1200px;height:2812px;overflow:hidden}
body{font-family:"Roboto",Arial,sans-serif;color:var(--text);background:var(--page);position:relative}

/* header */
.site-header{position:absolute;left:0;top:0;width:1200px;height:68px;background:var(--red)}
.brand{position:absolute;left:200px;top:16px;color:var(--white);font-size:28px;font-weight:500;letter-spacing:.5px}
.main-nav{position:absolute;right:200px;top:26px;display:flex;gap:34px}
.main-nav a{color:var(--white);text-decoration:none;font-size:14px;font-weight:700;letter-spacing:1px}

/* hero */
.hero{position:absolute;left:0;top:68px;width:1200px;height:320px;background:linear-gradient(#fafafa,#e9e9e9)}
.hero-title{position:absolute;left:284px;top:66px;font-weight:300;font-size:60px;line-height:56px;color:#444}
.hero-title strong{font-weight:500;color:var(--ink)}
.hero-portrait{position:absolute;left:720px;top:0;width:240px;height:320px;background:linear-gradient(180deg,#f3f3f3 0%,#d9c8bd 35%,#d63a3f 70%,#b8262c 100%)}

/* optin band */
.optin{position:absolute;left:0;top:388px;width:1200px;height:120px;background:var(--red)}
.optin-visual{position:absolute;left:244px;top:-52px;width:156px;height:150px;background:linear-gradient(#222 0%,#444 60%,#bbb 100%);border-radius:6px}
.optin-copy{position:absolute;left:424px;top:22px;width:500px;color:var(--white);font-size:15px;line-height:20px;font-weight:700;text-align:center}
.optin-copy em{font-style:normal;color:#ffe34d}
.optin-form{position:absolute;left:470px;top:70px;display:flex;gap:10px;align-items:center}
.field{width:160px;height:30px;background:var(--white);border-radius:15px;font-size:12px;color:var(--muted);padding:8px 14px}
.go{width:56px;height:56px;border-radius:50%;background:var(--ink);color:var(--white);font-weight:900;font-size:15px;display:flex;align-items:center;justify-content:center;border:3px solid var(--white)}
.optin-note{position:absolute;left:0;top:516px;width:1200px;text-align:center;font-size:11px;color:var(--muted)}

/* posts */
.post{position:absolute;left:212px;width:516px;height:440px;overflow:hidden;background:var(--white);box-shadow:0 1px 3px rgba(0,0,0,.12);padding:28px}
.post-media{position:relative;height:210px;overflow:hidden}
.post-media .photo{position:absolute;right:0;top:0;width:180px;height:100%}
.post-media .kicker{position:absolute;left:22px;top:34px;color:var(--white);font-weight:300;font-size:32px;line-height:38px;text-transform:uppercase}
.post-media .kicker b{font-weight:700}
.post-title{margin-top:16px;font-size:22px;line-height:28px;font-weight:400;color:#444}
.post-excerpt{margin-top:8px;font-size:12px;line-height:18px;color:var(--muted)}
.read-more{display:inline-block;margin-top:12px;font-size:12px;font-weight:700;color:var(--red);text-decoration:none}
.m-red{background:linear-gradient(90deg,#d9303a,#ef5a4f)}
.m-blue{background:linear-gradient(90deg,#2f47a8,#4f69cf)}
.m-slate{background:linear-gradient(90deg,#2f3b46,#4a5866)}
.m-tan{background:linear-gradient(90deg,#8a7758,#b3a07c)}

/* sidebar */
.sidebar{position:absolute;left:752px;top:560px;width:248px}
.widget-head{height:60px;background:var(--red);color:var(--white);font-weight:900;font-size:22px;display:flex;align-items:center;justify-content:center;letter-spacing:.5px}
.widget-body{background:var(--white);padding:16px 18px;box-shadow:0 1px 3px rgba(0,0,0,.12)}
.widget-label{text-align:center;color:var(--red);font-size:12px;font-weight:700;letter-spacing:1px;margin-bottom:10px}
.quote{font-size:11px;line-height:15px;color:#666;text-align:center;margin-bottom:4px}
.quote-link{display:block;text-align:center;font-size:10px;color:var(--red);margin-bottom:12px;text-decoration:none}
.tags{display:flex;flex-wrap:wrap;gap:4px;justify-content:center}
.tags span{font-size:11px;padding:2px 5px;color:var(--white);font-weight:700}
.tags .lg{font-size:20px}
.event-promo{position:relative;margin:32px auto 0;width:208px;height:488px;background:linear-gradient(180deg,#1e1e1e,#3a3a3a 60%,#1a1a1a)}
.event-promo .promo-text{position:absolute;left:0;top:58px;width:100%;text-align:center;color:var(--white);font-weight:900;font-size:22px;line-height:26px}
.event-promo .promo-text em{font-style:normal;color:var(--red)}
.event-promo .live{position:absolute;left:0;top:300px;width:100%;text-align:center;color:var(--white);font-weight:900;font-size:48px}
.event-promo .badge{position:absolute;left:64px;top:392px;width:80px;height:80px;border-radius:50%;background:var(--red);color:var(--white);font-size:12px;font-weight:900;display:flex;align-items:center;justify-content:center;text-align:center;line-height:14px}

/* pager */
.pager{position:absolute;left:212px;top:2398px;width:516px;display:flex;justify-content:center;gap:8px}
.pager i{width:14px;height:14px;border-radius:50%;background:#c9c9c9;display:block}
.pager i.on{background:var(--red)}
.pager i.dark{background:#666}

/* signup */
.signup{position:absolute;left:0;top:2444px;width:1200px;height:236px;background:var(--red);text-align:center;color:var(--white)}
.signup h2{margin-top:40px;font-size:17px;line-height:24px;font-weight:700}
.signup-form{margin-top:20px;display:flex;justify-content:center;gap:10px;align-items:center}
.signup .smile{margin-top:14px;font-size:13px;font-style:italic;color:#ffe0e0}

/* footer */
.site-footer{position:absolute;left:0;top:2680px;width:1200px;height:132px;background:var(--footer);color:#aaa;text-align:center}
.social{display:flex;justify-content:center;gap:10px;margin-top:28px}
.social i{width:34px;height:34px;border-radius:50%;background:#4a4a4a;display:block}
.footer-links{margin-top:26px;font-size:11px;display:flex;justify-content:center;gap:60px}
</style>
</head>
<body>

<header class="site-header">
  <div class="brand">Marla Penrick</div>
  <nav class="main-nav">
    <a href="#">HOME</a><a href="#">WORK WITH ME</a><a href="#">CORPORATE</a><a href="#">SHOP</a><a href="#">CONTACT</a>
  </nav>
</header>

<section class="hero">
  <h1 class="hero-title">Attract<br><strong>Connect</strong><br>Influence</h1>
  <div class="hero-portrait" role="img" aria-label="Marla standing in a red dress, smiling"></div>
</section>

<section class="optin">
  <div class="optin-visual" role="img" aria-label="Computer monitor showing a training video of Marla"></div>
  <p class="optin-copy">Learn how to unlock the superpower of your charisma and use it in the business you want with this <em>FREE training</em></p>
  <div class="optin-form">
    <div class="field">First name</div>
    <div class="field">Email address</div>
    <div class="go">GO!</div>
  </div>
</section>
<p class="optin-note">*Protected and you can opt-out at any time</p>

<article class="post" style="top:560px">
  <div class="post-media m-red">
    <p class="kicker">Public<br><b>speaking...</b><br>made <b>easy :)</b></p>
    <div class="photo" role="img" aria-label="Marla speaking with a microphone" style="background:linear-gradient(90deg,rgba(0,0,0,0),rgba(120,20,25,.5))"></div>
  </div>
  <h2 class="post-title">Public speaking...made easy</h2>
  <p class="post-excerpt">Nerves before a talk are normal. Here is how to turn that jittery energy into presence, warmth and a voice your audience wants to hear, with five simple habits you can practise this week before any meeting.</p>
  <a class="read-more" href="#">KEEP READING ▸</a>
</article>

<article class="post" style="top:1018px">
  <div class="post-media m-blue">
    <p class="kicker">How to start<br><b>every day</b><br>in the right<br><b>frame of mind!</b></p>
    <div class="photo" role="img" aria-label="Portrait of Marla smiling" style="background:linear-gradient(90deg,rgba(0,0,0,0),rgba(20,30,90,.45))"></div>
  </div>
  <h2 class="post-title">How to start every day in the right</h2>
  <p class="post-excerpt">The first hour shapes the whole day. Try this short morning routine to set your mood, clear your head and walk into every room feeling calm, bright and ready to connect with the people who matter.</p>
  <a class="read-more" href="#">KEEP READING ▸</a>
</article>

<article class="post" style="top:1476px">
  <div class="post-media m-slate">
    <p class="kicker">Take charge of<br><b>your style...</b><br>boost your<br><b>confidence</b></p>
    <div class="photo" role="img" aria-label="Red clothing card with a smiling woman" style="background:linear-gradient(90deg,rgba(0,0,0,0),rgba(200,40,50,.45))"></div>
  </div>
  <h2 class="post-title">Take charge of your style...Boost your confidence</h2>
  <p class="post-excerpt">Your clothes speak before you do. Learn how colour, fit and a few signature pieces can lift your confidence, sharpen your message and help people remember you long after the first hello is over.</p>
  <a class="read-more" href="#">KEEP READING ▸</a>
</article>

<article class="post" style="top:1934px">
  <div class="post-media m-tan">
    <p class="kicker">Unfulfilled?<br><b>It's time to think<br>about your values...</b><br>do this <b>exercise now!</b></p>
    <div class="photo" role="img" aria-label="Marla gesturing while talking" style="background:linear-gradient(90deg,rgba(0,0,0,0),rgba(60,45,30,.5))"></div>
  </div>
  <h2 class="post-title">Unfulfilled? It's time to think about your values...</h2>
  <p class="post-excerpt">When work feels flat, it often means your values are not being met. This quick exercise helps you name what matters most, so you can make choices that feel right and bring back your spark.</p>
  <a class="read-more" href="#">KEEP READING ▸</a>
</article>

<aside class="sidebar">
  <div class="widget-head">MARLA SAYS...</div>
  <div class="widget-body">
    <p class="widget-label">POPULAR</p>
    <p class="quote">"Be brave, be warm, and people will lean in."</p><a class="quote-link" href="#">READ ON</a>
    <p class="quote">"Your voice is your most loyal ally on stage."</p><a class="quote-link" href="#">READ ON</a>
    <p class="quote">"Confidence grows every time you show up."</p><a class="quote-link" href="#">READ ON</a>
    <p class="quote">"Smile first, then let the room come to you."</p><a class="quote-link" href="#">READ ON</a>
    <p class="widget-label" style="margin-top:6px">TAGS</p>
    <div class="tags">
      <span style="background:#e5202a">charisma</span><span style="background:#3d55b8">voice</span>
      <span class="lg" style="background:#2b2b2b">capture wardrobe</span>
      <span style="background:#9c8a6a">values</span><span style="background:#e5202a">style</span><span style="background:#3d4a57">stage</span>
      <span class="lg" style="background:#e5202a">confidence</span>
      <span style="background:#3d55b8">habits</span><span style="background:#2b2b2b">speaking</span>
      <span class="lg" style="background:#9c8a6a">rapport</span><span style="background:#3d4a57">mindset</span>
    </div>
  </div>
  <div class="widget-head" style="margin-top:36px">COMING UP</div>
  <div class="event-promo" role="img" aria-label="Event poster with Marla on stage in front of an audience">
    <p class="promo-text">UNLOCK<br>THE<br><em>SUPERPOWER</em><br>OF YOUR<br><em>CHARISMA</em></p>
    <p class="live">LIVE</p>
    <div class="badge">ONLY 8<br>PLACES<br>LEFT</div>
  </div>
</aside>

<nav class="pager" aria-label="Pages"><i class="on"></i><i></i><i></i><i></i><i class="dark"></i></nav>

<section class="signup">
  <h2>Hey! Don't go without signing up because you'll miss out on exclusive offers,<br>awesome tips, and weekly motivation in my fab newsletter *.</h2>
  <div class="signup-form">
    <div class="field">First name</div>
    <div class="field">Email address</div>
    <div class="go">GO!</div>
  </div>
  <p class="smile">* And that'll make me smile! :)</p>
</section>

<footer class="site-footer">
  <div class="social"><i></i><i></i><i></i><i></i><i></i></div>
  <div class="footer-links"><span>© 2014 Marla Penrick Ltd</span><span>Terms &amp; Privacy</span><span>Site Credits</span></div>
</footer>

</body>
</html>
```